Modern brochure by Lawyers, for modern clients

It'sa "News" for their clients. Attached you can find the current News without design. It must be elegant but very attractive and modern. Their web site is http://www.montealtoyasociados.cl/ Their expertise is labor and employment practice area. It must be in editable format so that lawyers can write the news in a template with this corporate design.

Target Market(s)

Big Companies

Font styles to use
Sans Serif

Colors
0255a3
474747

Requirements
Nice to have
• Legal Pictures and only a little of yellow. One touch! It must be in editable format so that lawyers can write the news in a template with this corporate design.

```html
<!DOCTYPE html>
<html lang="es">
<head>
<meta charset="utf-8">
<title>Montealto &amp; Asociados — Noticias</title>
<link href="https://fonts.googleapis.com/css2?family=Mulish:wght@400;600;700;800&display=swap" rel="stylesheet">
<style>
  :root {
    --brand-blue: #0255a3;
    --brand-navy: #1d3a6b;
    --text-gray: #474747;
    --accent-yellow: #d9d23a;
    --stage: #e9edf2;
    --paper: #ffffff;
    --rule: #e3e6ea;
    --footer-tint: #e4ecf5;
  }
  * { box-sizing: border-box; margin: 0; padding: 0; }
  html, body { width: 1200px; height: 954px; overflow: hidden; }
  body {
    background: var(--stage);
    font-family: "Mulish", sans-serif;
    color: var(--text-gray);
    display: flex;
    justify-content: center;
    align-items: center;
  }
  .newsletter {
    position: relative;
    width: 675px;
    height: 954px;
    background: var(--paper);
    display: flex;
    flex-direction: column;
    border-bottom: 4px solid var(--brand-blue);
  }
  .header-photo {
    height: 150px;
    border-top: 3px solid var(--accent-yellow);
    background: linear-gradient(100deg, #c9b79a 0%, #d8cdb8 30%, #b9a88c 55%, #d6cbb6 80%, #c4b395 100%);
  }
  .masthead {
    display: flex;
    justify-content: space-between;
    align-items: center;
    padding: 22px 44px 18px;
    border-bottom: 1px solid var(--rule);
  }
  .brand {
    display: flex;
    align-items: center;
    gap: 12px;
  }
  .brand-dot {
    width: 34px; height: 34px;
    border-radius: 50%;
    background: var(--brand-navy);
  }
  .brand-name {
    font-weight: 400;
    color: var(--brand-navy);
    font-size: 15px;
    letter-spacing: 3px;
    line-height: 1.2;
    text-transform: uppercase;
  }
  .issue-date {
    display: flex;
    align-items: center;
    gap: 10px;
    color: var(--brand-blue);
    font-weight: 700;
    font-size: 12px;
    text-align: right;
    line-height: 1.3;
  }
  .issue-date svg { flex: none; }
  .content {
    flex: 1;
    padding: 30px 44px 0;
    font-size: 12.5px;
    line-height: 1.55;
  }
  .greeting {
    color: var(--brand-blue);
    font-weight: 800;
    font-size: 14px;
    margin-bottom: 8px;
  }
  .content p { margin-bottom: 14px; }
  .content a { color: var(--brand-blue); font-weight: 600; }
  .closing { margin-top: 22px; }
  .signature-band {
    position: relative;
    height: 190px;
    background: linear-gradient(180deg, var(--paper) 0%, var(--footer-tint) 100%);
    display: flex;
    align-items: flex-end;
    padding: 0 44px 28px;
  }
  .side-photo {
    position: absolute;
    right: 0; top: 0;
    width: 200px; height: 120px;
    background: linear-gradient(135deg, #d4d6d8, #eef0f1);
  }
  .side-brand {
    position: absolute;
    right: 18px; top: 86px;
    display: flex; align-items: center; gap: 6px;
    font-size: 8px; letter-spacing: 1.5px;
    color: var(--brand-navy); text-transform: uppercase;
  }
  .side-brand span.dot {
    width: 12px; height: 12px; border-radius: 50%; background: var(--brand-navy);
  }
  .signature {
    display: flex;
    align-items: center;
    gap: 14px;
  }
  .avatar {
    width: 64px; height: 64px;
    border-radius: 50%;
    border: 3px solid var(--brand-navy);
    background: linear-gradient(160deg, #9aa6b3, #55606d);
  }
  .firm-name {
    color: var(--brand-blue);
    font-weight: 800;
    font-size: 17px;
  }
  .firm-email {
    display: flex; align-items: center; gap: 7px;
    font-size: 13px; color: var(--text-gray);
    margin-top: 3px;
  }
</style>
</head>
<body>
  <article class="newsletter">
    <div class="header-photo" role="img" aria-label="Fotografía de profesionales reunidos alrededor de una mesa de trabajo"></div>

    <header class="masthead">
      <div class="brand">
        <span class="brand-dot"></span>
        <span class="brand-name">Montealto<br>y Asociados Abogados</span>
      </div>
      <div class="issue-date">
        <span>Santiago,<br>25 de julio de 2018</span>
        <svg width="22" height="22" viewBox="0 0 22 22" aria-hidden="true">
          <circle cx="11" cy="11" r="11" fill="#0255a3"/>
          <rect x="6" y="7" width="10" height="9" rx="1" fill="none" stroke="#fff" stroke-width="1.3"/>
          <line x1="6" y1="10" x2="16" y2="10" stroke="#fff" stroke-width="1.3"/>
        </svg>
      </div>
    </header>

    <section class="content">
      <p class="greeting">Estimados,</p>
      <p>Por medio del presente, les damos a conocer el Dictamen Ordinario Nº 3826-031, emitido por la Dirección del Trabajo el pasado 20 de julio, relativo a los “beneficios históricos”.</p>
      <p>Estos fueron definidos en su oportunidad por este organismo como “…aquellos beneficios que se han otorgado desde siempre…” por parte del empleador.</p>
      <p>A partir de este Dictamen, el cual reconsidera el criterio del anterior Director del Trabajo, los beneficios históricos vuelven a ser patrimonio de la empresa y de los trabajadores que los han recibido, dejando de serlo de la organización sindical y de sus socios beneficiados por el solo hecho de “haberse replicado” en un instrumento colectivo durante una negociación.</p>
      <p>Por último, el Dictamen en comento aclara que si un “beneficio histórico” se incrementa de manera real y efectiva producto de una negociación colectiva, únicamente dicho incremento se entenderá originado en el respectivo instrumento colectivo, y en consecuencia, objeto de una posible extensión en el evento de que ésta se haya acordado durante la negociación.</p>
      <p>Para mayor análisis de lo resuelto por la Dirección del Trabajo, se puede revisar el Dictamen en comento haciendo <a href="http://www.montealtoyasociados.cl/">click aquí</a></p>
      <p class="closing">Sin otro particular, saluda atentamente a ustedes,</p>
    </section>

    <footer class="signature-band">
      <div class="side-photo" role="img" aria-label="Fotografía de documentos legales sobre un escritorio"></div>
      <div class="side-brand"><span class="dot"></span>Montealto y Asociados</div>
      <div class="signature">
        <div class="avatar" role="img" aria-label="Retrato del abogado socio"></div>
        <div>
          <div class="firm-name">Montealto &amp; Asociados</div>
          <div class="firm-email">
            <svg width="18" height="18" viewBox="0 0 18 18" aria-hidden="true">
              <circle cx="9" cy="9" r="9" fill="#1d3a6b"/>
              <rect x="4" y="5.5" width="10" height="7" rx="1" fill="#fff"/>
              <polyline points="4.5,6 9,9.8 13.5,6" fill="none" stroke="#1d3a6b" stroke-width="1.2"/>
            </svg>
            oficina@montealtoyasociados.cl
          </div>
        </div>
      </div>
    </footer>
  </article>
</body>
</html>
```